Contractor Business Card Design

Looking to have a card made that has a bold description of (KITCHENS, BASEMENTS, BATHROOMS)

Definition and layers a plus

Contact info is;

Mark T. Ellery
Larkfield, MN 55300
Cell: 612-555-0147
website: www.cobaltfinishworks.example
Email: cobaltfinishworksmn@mailbox.example

colors: red, black, gray, white

Contact Information for Business Card

Contact info is;

Mark T. Ellery
Larkfield, MN 55300
Cell: 612-555-0147

Colors
ec1f27

Requirements
Must have
• Looking for layers and definition
Nice to have
• Cards are planned to be printed on plastic cards

```html
<!DOCTYPE html>
<html lang="en">
<head>
<meta charset="utf-8">
<title>Cobalt Finish Works – Business Card</title>
<link href="https://fonts.googleapis.com/css2?family=Josefin+Sans:wght@400;700&family=Courgette&display=swap" rel="stylesheet">
<style>
  :root {
    --brand-red: #ec1f27;
    --ink-black: #111111;
    --plastic-gray: #e4e5e7;
    --stage-gray: #3b3d42;
    --paper-white: #ffffff;
  }
  * { margin: 0; padding: 0; box-sizing: border-box; }
  html, body {
    width: 1200px;
    height: 1200px;
    overflow: hidden;
    background: var(--stage-gray);
  }
  .business-card {
    position: absolute;
    left: 100px;
    top: 315px;
    width: 1000px;
    height: 570px;
    overflow: hidden;
    background: var(--plastic-gray);
  }
  .card-art {
    position: absolute;
    inset: 0;
    width: 1000px;
    height: 570px;
  }
  .holder-name {
    position: absolute;
    left: 50px;
    top: 242px;
    font-family: "Courgette", cursive;
    font-weight: 400;
    font-size: 46px;
    color: var(--paper-white);
    white-space: nowrap;
  }
  .contact-list {
    position: absolute;
    left: 50px;
    top: 372px;
    list-style: none;
    font-family: "Josefin Sans", sans-serif;
    font-size: 20px;
    color: var(--paper-white);
  }
  .contact-item {
    display: flex;
    align-items: center;
    height: 40px;
    white-space: nowrap;
  }
  .contact-icon {
    width: 22px;
    height: 22px;
    margin-right: 8px;
    flex: none;
  }
  .brand-lockup {
    position: absolute;
    left: 590px;
    top: 40px;
    width: 400px;
    display: flex;
    flex-direction: column;
    align-items: center;
  }
  .brand-circle {
    width: 160px;
    height: 160px;
    border-radius: 50%;
    border: 6px solid var(--brand-red);
  }
  .brand-name {
    margin-top: 26px;
    font-family: "Josefin Sans", sans-serif;
    font-weight: 700;
    font-size: 40px;
    line-height: 1.1;
    letter-spacing: 2px;
    text-align: center;
    color: var(--ink-black);
  }
</style>
</head>
<body>
  <article class="business-card">
    <svg class="card-art" viewBox="0 0 1000 570" aria-hidden="true">
      <path class="red-panel" d="M0 0 H390 Q640 285 400 570 H0 Z" fill="var(--brand-red)"/>
      <circle class="panel-ring" cx="230" cy="190" r="170" fill="none" stroke="#ffffff" stroke-opacity="0.14" stroke-width="14"/>
      <path class="panel-edge" d="M396 0 Q648 285 406 570" fill="none" stroke="var(--ink-black)" stroke-width="16"/>
    </svg>

    <h1 class="holder-name">Mark T. Ellery</h1>

    <ul class="contact-list">
      <li class="contact-item">
        <svg class="contact-icon" viewBox="0 0 24 24"><circle cx="12" cy="12" r="10" fill="none" stroke="#fff" stroke-width="2"/><path d="M8.5 7.5l2 2-1 1.5c.8 1.6 1.9 2.7 3.5 3.5l1.5-1 2 2-1.5 1.5c-3.5-.5-7-4-7.5-7.5z" fill="#fff"/></svg>
        612-555-0147
      </li>
      <li class="contact-item">
        <svg class="contact-icon" viewBox="0 0 24 24"><circle cx="12" cy="12" r="10" fill="none" stroke="#fff" stroke-width="2"/><path d="M12 6a4 4 0 0 1 4 4c0 3-4 8-4 8s-4-5-4-8a4 4 0 0 1 4-4z" fill="#fff"/><circle cx="12" cy="10" r="1.5" fill="var(--brand-red)"/></svg>
        Larkfield, MN 55300
      </li>
      <li class="contact-item">
        <svg class="contact-icon" viewBox="0 0 24 24"><circle cx="12" cy="12" r="10" fill="none" stroke="#fff" stroke-width="2"/><rect x="7" y="8.5" width="10" height="7" fill="#fff"/><path d="M7 8.5l5 4 5-4" fill="none" stroke="var(--brand-red)" stroke-width="1.2"/></svg>
        cobaltfinishworksmn@mailbox.example
      </li>
      <li class="contact-item">
        <svg class="contact-icon" viewBox="0 0 24 24"><circle cx="12" cy="12" r="10" fill="none" stroke="#fff" stroke-width="2"/><circle cx="12" cy="12" r="5.5" fill="none" stroke="#fff" stroke-width="1.5"/><path d="M6.5 12h11M12 6.5c-2 2.8-2 8.2 0 11M12 6.5c2 2.8 2 8.2 0 11" fill="none" stroke="#fff" stroke-width="1.2"/></svg>
        www.cobaltfinishworks.example
      </li>
    </ul>

    <div class="brand-lockup">
      <div class="brand-circle"></div>
      <p class="brand-name">COBALT<br>FINISH WORKS</p>
    </div>
  </article>
</body>
</html>
```